Business Card for Mortuary

We need a business card design for our mortuary. We are not the "traditional" mortuary and specialize in simple cremations and burials. We use a two sided card.

Industry/Entity Type

Funeral Home

Contact Information for Business Card

One side we would like to have with the general information of the mortuary:
Address: 4127 E. Larkspur Ave, Cedar Hollow, NM 87999
Phone: 623-555-0142
email: hello@willowbendmortuary.example
website: willowbendmortuary.example

On the other side would like to have the information of employee:
Name: Mark T. Ellis
Email: mark@willowbendmortuary.example
Title: Funeral Director
Text: 602-555-0187

Font styles to use
Serif
Sans Serif

Requirements
Should not have
• Do not put any gothic images or things like a hearse or tombstone.

```html
<!DOCTYPE html>
<html lang="en">
<head>
<meta charset="utf-8">
<title>Willowbend Mortuary – Business Card</title>
<link href="https://fonts.googleapis.com/css2?family=Source+Sans+3:wght@400;600;700&display=swap" rel="stylesheet">
<style>
  :root {
    --backdrop: #e6e6e6;
    --card-dark: #0a0a0a;
    --card-light: #f4f4f4;
    --green: #7dc242;
    --green-light: #b5d334;
    --ink: #1a1a1a;
    --ink-soft: #333333;
    --white: #ffffff;
  }
  * { margin: 0; padding: 0; box-sizing: border-box; }
  html, body { width: 1200px; height: 960px; overflow: hidden; }
  body {
    background: var(--backdrop);
    font-family: "Source Sans 3", Arial, sans-serif;
    position: relative;
  }
  .card {
    position: absolute;
    left: 318px;
    width: 570px;
    height: 325px;
    border-radius: 18px;
    overflow: hidden;
  }
  .card--front { top: 130px; background: var(--card-dark); color: var(--white); }
  .card--back { top: 505px; background: var(--card-light); color: var(--ink); }

  .frame {
    position: absolute;
    left: 28px; top: 27px;
    width: 513px; height: 270px;
    border: 2px solid var(--green);
    border-radius: 12px;
  }
  .frame__address {
    position: absolute;
    left: 50%; bottom: -10px;
    transform: translateX(-50%);
    background: var(--card-dark);
    padding: 0 8px;
    font-size: 14.5px;
    line-height: 18px;
    white-space: nowrap;
  }

  .brand { position: absolute; display: flex; align-items: center; }
  .brand__mark { border-radius: 50%; background: var(--green); flex: none; }
  .brand__name {
    font-weight: 700;
    line-height: 0.92;
    text-transform: uppercase;
    letter-spacing: -0.5px;
  }
  .brand__tagline {
    border-left: 1.5px solid var(--green);
    color: var(--green);
    line-height: 1.2;
  }

  .card--front .brand { left: 80px; top: 124px; }
  .card--front .brand__mark { width: 38px; height: 38px; margin-right: 30px; }
  .card--front .brand__name { font-size: 35px; color: var(--white); padding-right: 7px; }
  .card--front .brand__tagline { font-size: 19px; padding-left: 6px; }

  .card--back .brand { left: 40px; top: 76px; }
  .card--back .brand__mark { width: 26px; height: 26px; margin-right: 20px; }
  .card--back .brand__name { font-size: 23px; color: var(--ink); padding-right: 5px; }
  .card--back .brand__tagline { font-size: 13px; padding-left: 4px; }

  .contact-list {
    position: absolute;
    font-size: 14.5px;
    line-height: 19px;
  }
  .card--front .contact-list {
    left: 0; right: 0; top: 228px;
    text-align: center;
  }
  .contact-item { display: inline-flex; align-items: center; gap: 4px; margin: 0 7px; white-space: nowrap; }
  .icon { width: 13px; height: 13px; fill: none; stroke: var(--green); stroke-width: 1.6; flex: none; }
  .icon--solid { fill: var(--green); stroke: none; }

  .person { position: absolute; left: 49px; top: 170px; }
  .person__name { color: var(--green); font-weight: 700; font-size: 20px; line-height: 24px; }
  .person__title { font-size: 14.5px; color: var(--ink-soft); line-height: 20px; }

  .card--back .contact-list { left: 48px; top: 243px; color: var(--ink-soft); }
  .card--back .contact-item { display: flex; margin: 0; }

  .accent-circle {
    position: absolute;
    left: 300px; top: 60px;
    width: 330px; height: 330px;
    border-radius: 50%;
    background: linear-gradient(135deg, var(--green-light), var(--green));
    opacity: 0.9;
  }
</style>
</head>
<body>

  <section class="card card--front" aria-label="Business card front">
    <div class="frame">
      <p class="frame__address">4127 E. Larkspur Ave, Cedar Hollow, NM 87999</p>
    </div>
    <div class="brand">
      <span class="brand__mark"></span>
      <div class="brand__name">Willowbend<br>Mortuary</div>
      <div class="brand__tagline">Affordable<br>Cremation<br>and Burial</div>
    </div>
    <div class="contact-list">
      <span class="contact-item">
        <svg class="icon icon--solid" viewBox="0 0 16 16"><path d="M3 1l3 3-1.5 2a8 8 0 0 0 5.5 5.5L12 10l3 3-2 2C6 15 1 10 1 3z"/></svg>623-555-0142
      </span>
      <span class="contact-item">
        <svg class="icon" viewBox="0 0 16 16"><rect x="1.5" y="3.5" width="13" height="9"/><path d="M1.5 3.5L8 9l6.5-5.5"/></svg>hello@willowbendmortuary.example
      </span><br>
      <span class="contact-item">
        <svg class="icon" viewBox="0 0 16 16"><circle cx="8" cy="8" r="6.5"/><path d="M1.5 8h13M8 1.5c-3 3.5-3 9.5 0 13M8 1.5c3 3.5 3 9.5 0 13"/></svg>willowbendmortuary.example
      </span>
    </div>
  </section>

  <section class="card card--back" aria-label="Business card back">
    <div class="accent-circle" role="img" aria-label="Large green brand accent shape"></div>
    <div class="brand">
      <span class="brand__mark"></span>
      <div class="brand__name">Willowbend<br>Mortuary</div>
      <div class="brand__tagline">Affordable<br>Cremation<br>and Burial</div>
    </div>
    <div class="person">
      <h1 class="person__name">Mark T. Ellis</h1>
      <p class="person__title">Funeral Director</p>
    </div>
    <div class="contact-list">
      <span class="contact-item">
        <svg class="icon" viewBox="0 0 16 16"><rect x="4" y="1" width="8" height="14" rx="1.5"/><path d="M7 12.5h2"/></svg>602-555-0187
      </span>
      <span class="contact-item">
        <svg class="icon" viewBox="0 0 16 16"><rect x="1.5" y="3.5" width="13" height="9"/><path d="M1.5 3.5L8 9l6.5-5.5"/></svg>mark@willowbendmortuary.example
      </span>
    </div>
  </section>

</body>
</html>
```